Business Card Design Project

I need a business card design for our new logo, please check the logo at the following link:
https://files.quorvane-share.com/s/p7tkwe3nq4zr81h/FernCove.png
The address on the business card:
Av. Olegário Tavares 418 sala 207
Barra da Tijuca, Rio de Janeiro, RJ
CEP: 24917-380
Brasil
Phone: +55 21 73408216
e-mail: rogerio@ferncove-exemplo.com.br
Updates
Thank you all for sending your designs, we will not provide feedback because there are too many designs, on December 3 we will pick the best design according to our point of view. Please keep posting.
Rogério
Industry/Entity Type
Business

```html
<!DOCTYPE html>
<html lang="pt-BR">
<head>
<meta charset="utf-8">
<title>FernCove – Business Card</title>
<link href="https://fonts.googleapis.com/css2?family=Montserrat:wght@600;700;800&family=Source+Sans+3:wght@400&display=swap" rel="stylesheet">
<style>
  :root {
    --backdrop: #d9d9d9;
    --card-yellow: #f3c200;
    --card-yellow-deep: #e2ad00;
    --card-glow: #fbf0c0;
    --ink: #1a1a1a;
    --accent-orange: #e8821a;
    --divider: #6b5a10;
    --illustration-tone: #3a3320;
  }
  * { margin: 0; padding: 0; box-sizing: border-box; }
  html, body {
    width: 1200px; height: 1200px; overflow: hidden;
    background: var(--backdrop);
  }
  .canvas {
    position: relative; width: 1200px; height: 1200px;
  }
  .card {
    position: absolute; left: 180px; width: 840px; height: 480px;
    background: radial-gradient(ellipse 60% 70% at 58% 45%, var(--card-glow) 0%, var(--card-yellow) 62%, var(--card-yellow-deep) 100%);
    box-shadow: 0 6px 18px rgba(0,0,0,0.18);
    overflow: hidden;
  }
  .card--front { top: 90px; }
  .card--back  { top: 630px; }

  .mascot-area {
    position: absolute;
    background: radial-gradient(ellipse at 50% 50%, var(--illustration-tone) 0%, rgba(58,51,32,0.55) 70%, rgba(58,51,32,0) 100%);
    border-radius: 50%;
  }
  .wordmark {
    position: absolute;
    font-family: "Montserrat", sans-serif;
    font-weight: 800;
    color: var(--ink);
    letter-spacing: -1px;
    white-space: nowrap;
  }

  /* front */
  .card--front .mascot-area { left: 300px; top: 70px; width: 250px; height: 180px; }
  .card--front .wordmark { left: 0; right: 0; text-align: center; top: 262px; font-size: 100px; }

  /* back */
  .card-header {
    position: absolute; left: 40px; top: 30px;
    display: flex; align-items: center; gap: 14px;
    font-family: "Montserrat", sans-serif; white-space: nowrap;
  }
  .holder-name { font-weight: 700; font-size: 32px; color: var(--ink); }
  .header-divider { width: 2px; height: 44px; background: var(--divider); transform: skewX(-12deg); }
  .holder-function { font-weight: 600; font-size: 24px; color: var(--accent-orange); margin-top: 14px; }

  .card--back .mascot-area { left: 60px; top: 100px; width: 240px; height: 190px; }
  .card--back .wordmark { left: 36px; top: 290px; font-size: 62px; }

  .contact-block {
    position: absolute; left: 440px; top: 200px;
    font-family: "Source Sans 3", sans-serif; font-size: 22px; line-height: 1.36;
    color: var(--ink);
    font-style: normal;
  }
</style>
</head>
<body>
<main class="canvas">
  <section class="card card--front" aria-label="Card front">
    <div class="mascot-area" role="img" aria-label="Brand mascot illustration area"></div>
    <div class="wordmark">FernCove</div>
  </section>

  <section class="card card--back" aria-label="Card back">
    <header class="card-header">
      <span class="holder-name">Firstname Lastname</span>
      <span class="header-divider"></span>
      <span class="holder-function">Function</span>
    </header>
    <div class="mascot-area" role="img" aria-label="Brand mascot illustration area"></div>
    <div class="wordmark">FernCove</div>
    <address class="contact-block">
      Av. Olegário Tavares 418 sala 207<br>
      Barra da Tijuca, Rio de Janeiro, RJ<br>
      CEP: 24917-380<br>
      Brasil<br>
      Phone: +55 21 73408216<br>
      e-mail: rogerio@ferncove-exemplo.com.br
    </address>
  </section>
</main>
</body>
</html>
```